THE ORCHARD BELOW book cover needed

Hello friends! I'm working toward self-publishing my first novel in the next few months, and I'm looking to have a professional-looking, 6 in x 9 in cover to go along with the ebook release. I’m not looking for much, but the key is that it must look professional. I don’t want decorative fonts, but I also don’t want it to just look like Helvetica or Times New Roman.The text for the cover should be:A TIME FOR GREATNESSKARLIS WILDEI have attached a few images to show you where my head is at. I created a book cover myself on paint that looks horribly amateur, but it draws inspiration from a HPM campaign poster(also attached) where the title of the novel comes from. If you can make that same kind of cover, but make it look professional, that would be amazing! If you have other, simple ideas, I am also very, very open.Attached as well are a couple of simple, recent book covers that I like. That is the kind of thing that I am looking for.If this goes well, I may do a paperback release. In that case, I may need to contact you again for an additional fee to create the rest of the wraparound design. In addition, the book is the first in a projected trilogy, so there may be opportunities for you in the future for sequel covers.About the book: THE ORCHARD BELOW is a gripping, standalone thriller with an exciting take on history, relationships, conspiracy theories, and the current, volatile political state of America. In the present day, new information surrounding the 1963 assassination of Harold P. Merrow comes to light and Teodor Vasquelle, a young, best-selling journalist still reconciling his success with his dark past, finds himself more personally connected than he ever could have expected. But the story becomes something even bigger when an assassination attempt on the current demagogic president sends the whole world of journalism into a scramble, and Teodor finds himself confronted by an extremely difficult question: Is democracy real, or has it been an illusion fostered by these secretive ‘Wardens of the Ledger’ since 1776? Travelling across Syria, Canada, and the United States of America, the story becomes more unbelievable—and more personal—as increasingly prominent figures begin to enter Teodor’s orbit, intent on keeping their secrets safe by whatever means necessary.

Colors

Designer to choose colors to be used in the design.

Requirements
Must have
• Text
• Simplicity
• Professional look
Should not have
• Cheap fonts
• Complicated images

```html
<!DOCTYPE html>
<html lang="en">
<head>
<meta charset="utf-8">
<title>The Orchard Below — Cover</title>
<link rel="stylesheet" href="https://fonts.googleapis.com/css2?family=Anton&family=Oswald:wght@500;600;700&display=swap">
<style>
  :root {
    --stage: #1f1f1f;
    --navy: #13234f;
    --ink-white: #f3f3f1;
    --flag-red: #d4232e;
    --flag-blue: #2c2f7a;
    --flag-white: #f5f5f5;
  }
  * { margin: 0; padding: 0; box-sizing: border-box; }
  html, body {
    width: 1200px;
    height: 905px;
    overflow: hidden;
    background: var(--stage);
  }
  .cover {
    position: absolute;
    left: 320px;
    top: 32px;
    width: 560px;
    height: 840px;
    background: var(--navy);
    overflow: hidden;
    color: var(--ink-white);
  }
  .flag-band {
    position: absolute;
    left: 0;
    top: 0;
    width: 560px;
    height: 300px;
  }
  .title {
    position: absolute;
    left: 0;
    top: 330px;
    width: 100%;
    text-align: center;
    text-transform: uppercase;
  }
  .title-top {
    display: flex;
    justify-content: center;
    align-items: flex-end;
    gap: 10px;
  }
  .title-small {
    font-family: "Oswald", sans-serif;
    font-weight: 700;
    font-size: 40px;
    line-height: 1;
    padding-bottom: 10px;
  }
  .title-large {
    font-family: "Anton", sans-serif;
    font-size: 116px;
    line-height: 1;
    letter-spacing: 1px;
  }
  .title-bottom {
    font-family: "Anton", sans-serif;
    font-size: 106px;
    line-height: 1.05;
    letter-spacing: 2px;
  }
  .star-row {
    position: absolute;
    left: 50%;
    top: 598px;
    transform: translateX(-50%);
    display: flex;
    gap: 16px;
  }
  .star-row svg { width: 24px; height: 24px; fill: var(--flag-red); }
  .label {
    position: absolute;
    left: 0;
    top: 660px;
    width: 100%;
    text-align: center;
    font-family: "Oswald", sans-serif;
    font-weight: 600;
    font-size: 16px;
    letter-spacing: 12px;
    text-transform: uppercase;
  }
  .author {
    position: absolute;
    left: 0;
    top: 692px;
    width: 100%;
    text-align: center;
    font-family: "Oswald", sans-serif;
    font-weight: 700;
    font-size: 50px;
    line-height: 1.5;
    letter-spacing: 14px;
    text-transform: uppercase;
  }
</style>
</head>
<body>
  <main class="cover">
    <svg class="flag-band" viewBox="0 0 560 300" role="img" aria-label="Painted brushstroke of the American flag, stars and stripes sweeping across the top of the cover">
      <defs>
        <linearGradient id="flagGradient" x1="0" y1="0" x2="1" y2="0.3">
          <stop offset="0" stop-color="var(--flag-blue)"/>
          <stop offset="0.35" stop-color="var(--flag-red)"/>
          <stop offset="0.6" stop-color="var(--flag-white)"/>
          <stop offset="1" stop-color="var(--flag-red)"/>
        </linearGradient>
      </defs>
      <path d="M0 0 H560 V150 C440 150 330 165 220 200 C140 228 70 260 20 290 L0 300 Z" fill="url(#flagGradient)"/>
    </svg>

    <h1 class="title">
      <span class="title-top">
        <span class="title-small">The</span>
        <span class="title-large">Orchard</span>
      </span>
      <span class="title-bottom">Below</span>
    </h1>

    <div class="star-row" aria-hidden="true">
      <svg viewBox="0 0 24 24"><polygon points="12,1 15,9 23,9 16.5,14 19,22 12,17 5,22 7.5,14 1,9 9,9"/></svg>
      <svg viewBox="0 0 24 24"><polygon points="12,1 15,9 23,9 16.5,14 19,22 12,17 5,22 7.5,14 1,9 9,9"/></svg>
      <svg viewBox="0 0 24 24"><polygon points="12,1 15,9 23,9 16.5,14 19,22 12,17 5,22 7.5,14 1,9 9,9"/></svg>
      <svg viewBox="0 0 24 24"><polygon points="12,1 15,9 23,9 16.5,14 19,22 12,17 5,22 7.5,14 1,9 9,9"/></svg>
      <svg viewBox="0 0 24 24"><polygon points="12,1 15,9 23,9 16.5,14 19,22 12,17 5,22 7.5,14 1,9 9,9"/></svg>
      <svg viewBox="0 0 24 24"><polygon points="12,1 15,9 23,9 16.5,14 19,22 12,17 5,22 7.5,14 1,9 9,9"/></svg>
      <svg viewBox="0 0 24 24"><polygon points="12,1 15,9 23,9 16.5,14 19,22 12,17 5,22 7.5,14 1,9 9,9"/></svg>
      <svg viewBox="0 0 24 24"><polygon points="12,1 15,9 23,9 16.5,14 19,22 12,17 5,22 7.5,14 1,9 9,9"/></svg>
      <svg viewBox="0 0 24 24"><polygon points="12,1 15,9 23,9 16.5,14 19,22 12,17 5,22 7.5,14 1,9 9,9"/></svg>
      <svg viewBox="0 0 24 24"><polygon points="12,1 15,9 23,9 16.5,14 19,22 12,17 5,22 7.5,14 1,9 9,9"/></svg>
    </div>

    <p class="label">A Novel</p>
    <p class="author">Brenno<br>Saltvik</p>
  </main>
</body>
</html>
```